Meadowlane Women's Health - patient info e-book

We require an easy-edit template for a patient e-book that can easily be converted into a pdf for distribution through our website.
**We will be using Adobe InDesign, so compatible designs ONLY will be considered**
Target Market(s)
Women aged 28-55
Industry/Entity Type
Health
Font styles to use
Sans Serif
Colors
886aae
b8a6cd
d3a5cc
b768aa
ffffff
ecdaeb
b868aa
fbd4d5
f59296
Requirements
Must have
- Editable fields for text
- Easy to convert to PDF
- Easy to insert/change stock photos
- Should incorporate the attached logo

```html
<!DOCTYPE html>
<html lang="en">
<head>
<meta charset="utf-8">
<title>For Your Health – Meadowlane Women's Health News</title>
<link rel="stylesheet" href="https://fonts.googleapis.com/css2?family=Open+Sans:wght@600;700&family=Crimson+Text:ital,wght@0,400;1,400&display=swap">
<style>
  :root {
    --brand-purple: #886aae;
    --brand-purple-dark: #7c5fa4;
    --title-pink: #f59296;
    --ink: #1c1c1c;
    --paper: #ffffff;
    --photo-light: #e9edf2;
    --photo-navy: #2b3550;
  }
  * { margin: 0; padding: 0; box-sizing: border-box; }
  html, body { width: 927px; height: 1200px; overflow: hidden; background: var(--paper); }
  .page { position: relative; width: 927px; height: 1200px; background: var(--paper); }

  .section-band {
    position: absolute; left: 0; top: 0; width: 927px; height: 95px;
    background: linear-gradient(180deg, var(--brand-purple) 0%, var(--brand-purple-dark) 100%);
    box-shadow: 0 3px 5px rgba(0,0,0,0.25);
  }
  .section-band h2 {
    position: absolute; left: 57px; top: 54px;
    font: 700 23px/1 "Open Sans", sans-serif; color: var(--paper);
  }

  .article-title {
    position: absolute; left: 53px; top: 132px;
    font: 700 47px/1 "Open Sans", sans-serif; color: var(--title-pink);
    letter-spacing: -0.3px;
  }

  .column {
    position: absolute; overflow: hidden;
    font: 400 15.4px/19.75px "Crimson Text", serif; color: var(--ink);
    text-align: justify; hyphens: auto;
  }
  .column p { text-indent: 27px; margin-bottom: 8px; }
  .column p.cont { text-indent: 0; }
  .col-1 { left: 57px; top: 228px; width: 252px; height: 872px; }
  .col-2 { left: 318px; top: 228px; width: 273px; height: 872px; }
  .col-3 { left: 618px; top: 592px; width: 255px; height: 510px; }

  .feature-photo {
    position: absolute; left: 618px; top: 246px; width: 255px; height: 297px;
    border: 1px solid #222;
    background: linear-gradient(180deg, var(--photo-light) 0%, var(--photo-light) 45%, var(--photo-navy) 75%, var(--photo-navy) 100%);
  }
  .photo-caption {
    position: absolute; left: 618px; top: 559px; width: 255px; text-align: center;
    font: italic 400 15.4px/1.2 "Crimson Text", serif; color: var(--ink);
  }

  .page-footer {
    position: absolute; left: 57px; right: 54px; top: 1145px;
    display: flex; justify-content: space-between;
    font: 600 15px/1 "Open Sans", sans-serif; color: var(--ink);
  }
  .page-footer .folio span { margin-left: 10px; }
</style>
</head>
<body>
<div class="page">
  <header class="section-band"><h2>For Your Health</h2></header>

  <h1 class="article-title">Peris aut modis sam quae</h1>

  <div class="column col-1">
    <p>Ore, sequia sam aut adi dicium ex est, officae cullabo rationsed que vendaes quiatum imentoribus eum lab il eium volum non numet reperchil inullac caborum ut exceati vente rae voluptatiis eum ipsa vendesciam doluptur. Em fuga. Ibuscid usdamus aut quatem nus.</p>
    <p>Edit harchit officil inverum etum sequi as pellique rem quibeat ecestiae. Tas eiur, consectus dolorecabo. Um volupti orenem excepe cullaudiate nihic te et a plabore que nonsed et aboribus maximus sandunt quod mod etur apis aut quasperem laborer spellest ea qui ommos pliciis ra vollessus quatem volorpor repedipsa plicipitate volorestium ut adionsedit, sunt apientem faccus audam el issintior aut quias dolupta prem everatiurit, occus et ped que volorpor maximi, officides aut Us eari dolupta si delluptas delestia doluptia quam autas consequunt, tempore pudanist, quiam, etur rerum a quiam audit que nonet, od moditam quis aut autem dolorem. Nam quia nis quamet mincient acculparibus seque con conem quissit ut officiunti blam explantur am doloreptat.</p>
    <p>Ces aute liqui ducit officitat ommoluptur aut re, sandipsant.</p>
    <p>Omnit ati omniend untempe libus, omnia volum eum cus est perror mod mo quistiasi dolupta voluptaquia vendandes ius sedit laborerum hitem simagnis id que nia qui doluptatur sequi aut volluptatem iumet volut entorec tassimo lorectas dellor aut ra pa et, sequatat.</p>
    <p>Poreste moditat volo beritam enimagnation culparum ex ellorume voluptatum sumquo erovitio eate sumet exerferferum nonetur molupta audis</p>
  </div>

  <div class="column col-2">
    <p class="cont">corecti dit que et eum dolestia cor repelest est et perioribusa con porisciis sapis et plit, qui opti odi aliquam quisim ut voluptatur sum quibus dolor molut que lam as earunt.</p>
    <p>Puda pa voluptaquae. Nam fugit maionsent quam rendiostrum idebit evelitatiis accuptaqui arum sequos everi coreped ut quossime dolorio vel ius, que endam expe sintoribus praturis coreicabore eatusda voloriat.</p>
    <p>Sunto dist aut faces maionsequi tesseca borempores doluptatem harchil eossimin es atquuntis ma pel molo min eos magnihil ilibeaque everfere nectota sus que sintius, tet hil essed earupta ius re dolupiet ut duciendunt ea suntum conetur aut qui aut qui dTem fugitium nonsecus sunt, natur autemos velent quoditibusam sit dolupieniet auda volupiciam vero doloremporem aliquat usapis essum aut quisci dolorem que volum nullibe atectem. Ximendis voluptat et parum et erist di doloris et eost laborum essumque perore omnis sin exeribusti idebis eum ut alita sit auta consequi dolest, vollaborum dioribernam conseCon reserum ressimi lloritis perum est istibustiam undit laboriate odit omnistis explic to doloribus.</p>
    <p>Perem. Et ra cullupt ioristis il moluptaes eribus.</p>
    <p>Rerumet maximusda sollaborro et volupta ipsunt rem. Te cust, tenis ea presciat.</p>
    <p>At fugias voluptat. Um, optatur, et aut aut latissunt rerspient a autempores sam quatem et ommolum que velique doluptae et laboriam harum solest, ut aut et rem dolupiciis atisserum aliciumet im quoditae qui do-</p>
  </div>

  <div class="feature-photo" role="img" aria-label="Stock photo of a smiling professional woman in a pinstripe suit seated at a desk"></div>
  <p class="photo-caption">Nam que pla simille catibus, siminis</p>

  <div class="column col-3">
    <p class="cont">lor adi officaerum veniet moluptatio. Mo et eosam quassim inctur raturis sum esti dolore quibus, odit qui occatem fuga. Nem quam acipsaped eat exerumq uatiscias cor simin nulparum volende simo essed qui in consequae late pa poriorepre, simporem int eostius quid utatisque volutem velis dolorem aut as ant, num nimaior alicimi, siti blam aboruptassi delibus, volliquo quo quasper ionseque cus et, tem fugia inctaque se rectem. Itata pre mod estrum lignis auditaquiae la volorum nonsequ amenis aute prerfer umquibusam, sunturest eossere lab inum alic tem qui aut ut laut inciaes eostiumquam res ut labo. Mus, quam siminctet alit fugitatia voluptae nihil iderect atiatur a ant delluptaque comnis ad qui nectis quae esti quatinctur, sit dolorei ciliatur aut et, qui beatur sequi doluptatur sae con cus conempore nihiciur? Qui nam, odi nat exerspe ni videbis acia aut volenis pos doluptas de plit resci blacepudit, sam explabo. Cus eatum il int, ipsam quosame tusdae nonsequi off</p>
  </div>

  <footer class="page-footer">
    <span class="publication">Meadowlane Women's Health News</span>
    <span class="folio">May 2015<span>3</span></span>
  </footer>
</div>
</body>
</html>
```